Software Company Banner Ad

We need a banner ad in two sizes. 728x90 and 300x250.
They should have strong similarity to the following ads:
http://www.trelvix.com/search/results?brand[0]=quorp&ad=5777135
http://www.trelvix.com/search/results?brand[0]=dalbrentix&ad=5789298
Idea will be very similar. We want the same grey color, white text, and a realistic owl that blinks. The owl should have dramatic, bright, yellow eyes. The text will animate "from the top" as in the example. Though the logo animation will be different, all text and non-logo animation should match the animation in the example advertisements. The text will rotate between the following four sentences and images.
Looking for a provider of procurement cloud apps?
[Images - attached below]
The experts really liked our KVP booth.
Get great results with every procurement. [Learn more]
There are three vector files attached below. Feel free to change the colors as necessary to match the color scheme of the ad. We need one 2013 and one 2014 award in the ad.
The awards could appear simultaneously, could swap with each other or could appear in succession. Animation is acceptable.
There is an additional vector file with the company logo. The company logo should go where the Quorp logo is in horizontal ad. The company logo should go where the Dalbrentix logo is in the block ad. The example ad has two logos. We will only need one logo on our ads. The logo should be changed to the color of the text used for the ad (white).
The owls eyes should slowly blink two times (as in the example).
The owl eyes should immediately grab someone's attention and all colors should compliment these eyes.
The [Learn more] button should have animation. The button should match the color of the owl's eyes. There should be a line/gleam/glare of light that travels across the button. The button should be embossed with the subtle animation occurring each time it appears.
Ads should be done with flash. We will need the source files and the names of any fonts used at the end of the project.
Thank you and please do not hesitate to contact with any questions.
Reason: We have contacted several photographers to see if the alternative owl images are available on Pixwarel, Framebaskit or similar. The duration extension is to accommodate this.
Target Market(s)
Target customers are procurement department employees of large companies.
Industry/Entity Type
It Company

```html
<!DOCTYPE html>
<html lang="en">
<head>
<meta charset="utf-8">
<title>TALVEN — Procurement Banner</title>
<link href="https://fonts.googleapis.com/css2?family=Roboto+Condensed:wght@700&display=swap" rel="stylesheet">
<style>
  :root {
    --bg-light: #8c8c8c;
    --bg-mid: #6e6e6e;
    --bg-dark: #5c5c5c;
    --band-dark: #4f4f4f;
    --text-white: #ffffff;
    --button-top: #b8f23c;
    --button-bottom: #6cb60c;
    --button-edge: #4a8606;
    --button-text: #1d3604;
    --icon-fill: #26460a;
    --photo-light: #e4e1da;
    --photo-mid: #aaa59b;
  }
  * { margin: 0; padding: 0; box-sizing: border-box; }
  html, body { width: 1200px; height: 148px; overflow: hidden; background: var(--bg-mid); }
  .banner {
    position: relative;
    width: 1200px;
    height: 148px;
    overflow: hidden;
    background: linear-gradient(180deg, var(--bg-mid) 0%, var(--bg-dark) 100%);
    font-family: "Roboto Condensed", "Arial Narrow", sans-serif;
    color: var(--text-white);
  }
  .corner-band { position: absolute; left: 0; top: 0; width: 280px; height: 148px; }
  .brand-name {
    position: absolute;
    left: 14px;
    top: 12px;
    font-size: 30px;
    line-height: 30px;
    font-weight: 700;
    letter-spacing: 1px;
    color: var(--text-white);
  }
  .headline {
    position: absolute;
    left: 241px;
    top: 24px;
    font-size: 36px;
    line-height: 38px;
    font-weight: 700;
    text-transform: uppercase;
    white-space: nowrap;
    transform: scaleX(0.87);
    transform-origin: left top;
  }
  .headline-line { display: block; }
  .cta-button {
    position: absolute;
    left: 460px;
    top: 69px;
    width: 221px;
    height: 48px;
    border-radius: 5px;
    border: 2px solid var(--button-edge);
    background: linear-gradient(180deg, var(--button-top) 0%, var(--button-bottom) 100%);
    box-shadow: inset 0 2px 0 rgba(255,255,255,0.45), 0 1px 2px rgba(0,0,0,0.35);
    display: flex;
    align-items: center;
    justify-content: center;
    gap: 14px;
    font-size: 22px;
    font-weight: 700;
    color: var(--button-text);
    text-transform: uppercase;
    letter-spacing: 0.5px;
  }
  .cta-icon { width: 25px; height: 25px; }
  .owl-photo {
    position: absolute;
    right: 0;
    top: 0;
    width: 430px;
    height: 148px;
    background: radial-gradient(ellipse at 65% 50%, var(--photo-light) 0%, var(--photo-mid) 55%, rgba(110,110,110,0) 100%);
    -webkit-mask-image: linear-gradient(90deg, transparent 0%, #000 25%);
            mask-image: linear-gradient(90deg, transparent 0%, #000 25%);
  }
</style>
</head>
<body>
  <div class="banner">
    <svg class="corner-band" viewBox="0 0 280 148" aria-hidden="true">
      <polygon points="0,0 228,0 0,138" fill="#8c8c8c"/>
      <polygon points="228,0 268,0 0,162 0,138" fill="#4f4f4f"/>
    </svg>

    <div class="brand-name">TALVEN</div>

    <h1 class="headline">
      <span class="headline-line">Get great results with every</span>
      <span class="headline-line">procurement.</span>
    </h1>

    <div class="cta-button">
      <span class="cta-label">Learn more</span>
      <svg class="cta-icon" viewBox="0 0 24 24" aria-hidden="true">
        <circle cx="12" cy="12" r="11" fill="#26460a"/>
        <path d="M10 7 L15 12 L10 17" fill="none" stroke="#b8f23c" stroke-width="3" stroke-linecap="round" stroke-linejoin="round"/>
      </svg>
    </div>

    <div class="owl-photo" role="img" aria-label="Photograph of a grey and white owl with bright green-yellow eyes"></div>
  </div>
</body>
</html>
```